Precise Finish Emulator (PFE)

I would like to design a dedicated site for my PFE product, which allows industry employees to be trained in the visual inspection of mechanical parts. My product is a 3D simulator (see https://norvik-works.ch/our-applications/virtual-reality/ and https://norvik-works.ch for videos) which makes it possible to manufacture standard parts representative of a type of defect which is accepted or refused by the quality department. These master parts can be used to create a common quality culture in the company and to train employees in a homogeneous way. The simulator is initially designed for watchmaking, but must be designed for much broader industries (cars, phone reconditioning, ball bearings, etc.)
L'information que j'ai donnée n'est pas assez précise. Je dois préciser les domaines métiers visés par le site internet. J'ai besoin de quelques jours pour choisir les domaines les plus représentatifs.

```html
<!DOCTYPE html>
<html lang="en">
<head>
<meta charset="utf-8">
<title>PFE – Precise Finish Emulator</title>
<link href="https://fonts.googleapis.com/css2?family=Oswald:wght@400;500;600;700&family=Poppins:ital,wght@0,400;0,500;1,400&display=swap" rel="stylesheet">
<style>
:root{
  --blue:#0a6fc2;
  --blue-dark:#085a9e;
  --ink:#222222;
  --dark:#232323;
  --grey:#e6e6e6;
  --text:#555555;
  --white:#ffffff;
}
*{margin:0;padding:0;box-sizing:border-box}
html,body{width:1200px;height:4399px;overflow:hidden}
body{position:relative;background:var(--white);font-family:"Poppins",sans-serif;color:var(--text)}
.abs{position:absolute}
.head{font-family:"Oswald",sans-serif;text-transform:uppercase;color:var(--ink);font-weight:600;letter-spacing:.5px}
.ph{position:absolute}
.btn{position:absolute;background:var(--blue);color:var(--white);font-family:"Oswald",sans-serif;font-size:14px;font-weight:500;text-transform:uppercase;display:flex;align-items:center;justify-content:center}

/* header */
.logo{left:90px;top:24px;font-family:"Oswald",sans-serif;font-weight:500;font-size:30px;color:var(--blue)}
.contact-chip{top:25px;height:36px;display:flex;align-items:center;gap:12px;font-family:"Oswald",sans-serif;font-size:14px;color:var(--ink)}
.chip-icon{width:36px;height:36px;background:var(--blue);display:flex;align-items:center;justify-content:center}
.search{left:888px;top:25px;width:222px;height:36px;background:#f0f0f0;font-size:12px;color:#888;padding:0 14px;display:flex;align-items:center;justify-content:space-between}
.nav{left:0;top:88px;width:1200px;height:50px;background:var(--dark);display:flex;justify-content:center;align-items:center;gap:17px}
.nav a{font-family:"Oswald",sans-serif;font-size:15px;color:var(--white);text-decoration:none;text-transform:uppercase}

/* hero */
.hero-title{left:90px;top:300px;font-family:"Oswald",sans-serif;font-weight:700;font-size:98px;line-height:96px;color:var(--white);text-transform:uppercase}
.hero-sub{left:90px;top:505px;font-family:"Oswald",sans-serif;font-size:27px;color:var(--white);text-transform:uppercase}
.hero-btn{left:90px;top:556px;width:145px;height:42px;background:var(--white);color:var(--ink);font-family:"Oswald",sans-serif;font-size:14px;font-weight:500;display:flex;align-items:center;justify-content:center}

/* about */
.about-title{left:578px;top:915px;font-size:50px}
.about-sub{left:578px;top:993px;font-family:"Oswald",sans-serif;font-size:13px;color:var(--ink);text-transform:uppercase}
.about-text{left:578px;top:1022px;width:470px;font-size:13px;line-height:23px}

.section-title{left:0;width:1200px;text-align:center;font-size:48px}
.card-label{position:absolute;bottom:26px;left:0;width:100%;text-align:center;font-family:"Oswald",sans-serif;font-weight:600;font-size:27px;color:var(--white);text-transform:uppercase}

.contact-ghost{left:0;top:2680px;width:1200px;text-align:center;font-family:"Oswald",sans-serif;font-weight:700;font-size:215px;line-height:220px;color:transparent;background:linear-gradient(#dcdcdc,#ffffff);-webkit-background-clip:text;background-clip:text;letter-spacing:4px}

.quote{left:0;top:3668px;width:1200px;text-align:center;font-size:19px;line-height:27px;font-style:italic;color:#555}
.author{left:0;top:3774px;width:1200px;text-align:center;font-family:"Oswald",sans-serif;font-size:17px;color:var(--blue);text-transform:uppercase}
.author-name{left:0;top:3803px;width:1200px;text-align:center;font-size:12px;color:#555}
.dot{position:absolute;left:1104px;width:9px;height:9px;border-radius:50%;background:#ccc}

/* footer */
.foot-logo{left:0;width:525px;top:4120px;text-align:center;font-family:"Oswald",sans-serif;font-size:46px;color:#bbbbbb}
.social{position:absolute;top:4189px;width:38px;height:38px;border-radius:50%;background:#3a3a3a}
.foot-col h4{font-family:"Oswald",sans-serif;font-size:17px;font-weight:500;color:var(--white);text-transform:uppercase;margin-bottom:20px}
.foot-col li{list-style:none;font-size:12px;color:#ddd;line-height:27px}
.info-row{display:flex;gap:10px;font-size:12px;color:#ddd;line-height:18px;margin-bottom:18px}
.copyright{left:0;top:4358px;width:1200px;text-align:center;font-family:"Oswald",sans-serif;font-size:12px;color:var(--white);text-transform:uppercase}
</style>
</head>
<body>

<!-- header -->
<div class="abs logo">PFE</div>
<div class="abs contact-chip" style="left:482px">
  <span class="chip-icon"><svg width="16" height="12" viewBox="0 0 16 12"><rect width="16" height="12" fill="#fff"/><path d="M0 0l8 6 8-6" stroke="#0a6fc2" stroke-width="1.6" fill="none"/></svg></span>HELLO@FINISHMAIL.CH
</div>
<div class="abs contact-chip" style="left:718px">
  <span class="chip-icon"><svg width="16" height="16" viewBox="0 0 24 24"><path fill="#fff" d="M6.6 10.8a15 15 0 006.6 6.6l2.2-2.2a1 1 0 011-.25 11.4 11.4 0 003.6.6 1 1 0 011 1V20a1 1 0 01-1 1A17 17 0 013 4a1 1 0 011-1h3.5a1 1 0 011 1c0 1.25.2 2.45.6 3.6a1 1 0 01-.25 1z"/></svg></span>(041) 555-0182
</div>
<div class="abs search">Search here...<svg width="12" height="12" viewBox="0 0 12 12"><circle cx="5" cy="5" r="3.8" stroke="#222" stroke-width="1.5" fill="none"/><path d="M8 8l3 3" stroke="#222" stroke-width="1.5"/></svg></div>
<nav class="abs nav"><a>In regards to</a><a>Services</a><a>Partners</a><a>References</a><a>Info</a><a>Contact</a></nav>

<!-- hero -->
<svg class="ph" style="left:0;top:138px" width="1200" height="730" viewBox="0 0 1200 730">
  <polygon points="0,680 1200,540 1200,730 0,730" fill="var(--grey)"/>
  <polygon points="0,0 1200,0 1200,542 0,672" fill="#2a2f36" role="img" aria-label="Photo of a machine with coloured cables and a red cylinder"/>
  <polygon points="600,0 1200,0 1200,300 700,200" fill="#3b3430" opacity=".7"/>
  <circle cx="1054" cy="556" r="56" fill="var(--blue)"/>
  <polygon points="1045,536 1045,576 1070,556" fill="#fff"/>
</svg>
<div class="abs hero-title">Finish<br>Emulator</div>
<div class="abs hero-sub">My product is a 3D simulator</div>
<div class="abs hero-btn">VIEW PRODUCTS</div>
<div class="ph" style="left:716px;top:740px;width:1px;height:155px;background:#cfcfcf"></div>

<!-- about -->
<svg class="ph" style="left:150px;top:1118px" width="276" height="274">
  <defs><pattern id="stripes" width="8" height="8" patternUnits="userSpaceOnUse" patternTransform="rotate(45)"><rect width="4" height="8" fill="var(--blue)"/></pattern></defs>
  <rect width="276" height="274" fill="url(#stripes)"/>
</svg>
<div class="ph" role="img" aria-label="Photo of an electronic circuit board on a blue frame" style="left:178px;top:898px;width:325px;height:470px;background:linear-gradient(135deg,#c9a24a,#2f5fa8 55%,#8aa7c4)"></div>
<div class="ph" role="img" aria-label="Photo of a yellow probe pen with coiled cable" style="left:985px;top:768px;width:215px;height:235px;background:linear-gradient(225deg,#e4e4e4,#f4f1d8 55%,#ffffff)"></div>
<div class="ph" style="left:555px;top:995px;width:20px;height:1px;background:#ccc"></div>
<div class="abs head about-title">About Company</div>
<div class="abs about-sub">Welcome to Precise Finish Emulator</div>
<p class="abs about-text">At vero eos et accusamus et iusto odio dignissimos ducimus qui blanditiis praesentium voluptatum deleniti atque corrupti quos dolores et quas molestias excepturi sint occaecati cupiditate non provident, similique sunt in culpa qui officia deserunt mollitia animi, id est laborum et dolorum fuga. Et harum quidem rerum facilis est et expedita distinctio. Nam libero tempore, cum soluta nobis est eligendi optio cumque nihil impedit quo minus id quod maxime placeat facere possimus, omnis voluptas assumenda est, omnis dolor repellendus. Temporibus autem quibusdam et aut officiis debitis aut rerum necessitatibus saepe eveniet ut et voluptates repudiandae sint et molestiae non recusandae.</p>
<div class="btn" style="left:578px;top:1290px;width:144px;height:42px">Learn More</div>

<!-- videos -->
<div class="abs head section-title" style="top:1508px">Watch Our Videos</div>
<div class="ph" role="img" aria-label="Video still of a technician testing an engine with a pressure gauge" style="left:230px;top:1595px;width:602px;height:400px;background:linear-gradient(120deg,#3a3d42,#6c7580 50%,#2b3f73)"></div>
<svg class="ph" style="left:519px;top:1784px" width="24" height="24"><polygon points="5,3 5,21 21,12" fill="#fff"/></svg>
<div class="ph" role="img" aria-label="Video thumbnail of industrial pipes" style="left:843px;top:1595px;width:128px;height:128px;background:linear-gradient(#6b5a45,#2f3a3f)"></div>
<div class="ph" role="img" aria-label="Video thumbnail of a worker checking stock on shelves" style="left:843px;top:1732px;width:128px;height:128px;background:linear-gradient(#4d7fb5,#c8d4df)"></div>
<div class="ph" role="img" aria-label="Video thumbnail of a worker repairing equipment" style="left:843px;top:1869px;width:128px;height:128px;background:linear-gradient(#7a4a3a,#3a3f55)"></div>

<!-- products -->
<svg class="ph" style="left:0;top:2116px" width="1200" height="460" viewBox="0 0 1200 460">
  <polygon points="0,0 1200,0 1200,440 0,220" fill="var(--blue)" role="img" aria-label="Blue band over a faint workshop photo"/>
  <polygon points="0,220 0,285 1200,470 1200,440" fill="#ececec"/>
</svg>
<div class="abs head section-title" style="top:2220px;color:#fff">Our Products</div>
<div class="ph" role="img" aria-label="Photo of a hand holding a microchip over a circuit board" style="left:90px;top:2313px;width:333px;height:320px;background:linear-gradient(160deg,#c9b8a2,#3d5f8f 70%,#1f2d45)"><span class="card-label">Heading Here</span></div>
<div class="ph" role="img" aria-label="Photo of a gloved technician working on a motherboard" style="left:435px;top:2313px;width:332px;height:320px;background:linear-gradient(160deg,#e0e0e0,#6e7d8c 60%,#2b3340)"><span class="card-label">Heading Here</span></div>
<div class="ph" role="img" aria-label="Photo of a technician soldering a circuit board" style="left:778px;top:2313px;width:333px;height:320px;background:linear-gradient(160deg,#7a6c5e,#4e6f9a 60%,#2a3445)"><span class="card-label">Heading Here</span></div>

<!-- contact -->
<div class="abs contact-ghost">CONTACT</div>
<div class="abs head section-title" style="top:2852px">Get In Touch With Us</div>
<div class="btn" style="left:527px;top:2918px;width:145px;height:42px">Contact Us</div>

<!-- gallery -->
<div class="ph" role="img" aria-label="Photo of a robotic arm touching water" style="left:0;top:3083px;width:240px;height:352px;background:linear-gradient(#e8edf2,#8fa6b8)"></div>
<div class="ph" role="img" aria-label="Photo of car bodies on an assembly line" style="left:240px;top:3083px;width:240px;height:352px;background:linear-gradient(#8a6a52,#3c4d6a)"></div>
<div class="ph" role="img" aria-label="Photo of a small robot kit on a workbench" style="left:480px;top:3083px;width:240px;height:352px;background:linear-gradient(#6e5b48,#2d2a27)"></div>
<div class="ph" role="img" aria-label="Photo of miniature workers on a circuit board" style="left:720px;top:3083px;width:240px;height:352px;background:linear-gradient(#a08f72,#2f3d66)"></div>
<div class="ph" role="img" aria-label="Photo of glowing gears on a circuit board" style="left:960px;top:3083px;width:240px;height:352px;background:radial-gradient(circle at 50% 45%,#d88a3a,#2c3338 45%,#1c2024)"></div>
<svg class="ph" style="left:545px;top:3234px" width="110" height="50">
  <circle cx="25" cy="25" r="24" fill="#fff"/><circle cx="85" cy="25" r="24" fill="#fff"/>
  <circle cx="23" cy="23" r="6" stroke="var(--blue)" stroke-width="2" fill="none"/><path d="M27 27l5 5" stroke="var(--blue)" stroke-width="2"/>
  <path d="M80 30l10-10M78 26l-2 2a4 4 0 006 6l2-2M92 24l2-2a4 4 0 00-6-6l-2 2" stroke="var(--blue)" stroke-width="2" fill="none"/>
</svg>

<!-- testimonials -->
<svg class="ph" style="left:145px;top:3590px" width="190" height="130">
  <path d="M5 120V70Q5 15 70 5v25Q35 35 40 60h40v60z M105 120V70Q105 15 170 5v25Q135 35 140 60h40v60z" fill="#f0f0f0"/>
</svg>
<div class="abs head section-title" style="top:3552px">Client's Testimonials</div>
<p class="abs quote">The RX 500 is an incredible piece of machinery and has proven very<br>reliable. Sometimes I laugh to myself when I realize a customer is paying me<br>a great hourly wage to have so much fun.</p>
<div class="abs author">- Dale Brennick Owner</div>
<div class="abs author-name">Mara Lintz</div>
<span class="dot" style="top:3666px"></span><span class="dot" style="top:3691px;background:#111"></span><span class="dot" style="top:3716px"></span>

<!-- footer -->
<svg class="ph" style="left:0;top:3850px" width="1200" height="549" viewBox="0 0 1200 549">
  <polygon points="1200,0 1200,60 0,175 0,150" fill="var(--grey)"/>
  <polygon points="1200,55 1200,549 0,549 0,160" fill="var(--dark)"/>
</svg>
<div class="abs foot-logo">PFE</div>
<span class="social" style="left:174px"></span><span class="social" style="left:221px"></span><span class="social" style="left:268px"></span><span class="social" style="left:315px"></span>
<div class="abs foot-col" style="left:465px;top:4050px"><h4>Quick Links</h4><ul><li>In regards to</li><li>Services</li><li>Partners</li><li>References</li><li>Info</li><li>Contact</li></ul></div>
<div class="abs foot-col" style="left:649px;top:4050px"><h4>Information</h4><ul><li>Privacy Policy</li><li>Terms &amp; Conditions</li><li>Shipping Policy</li><li>FAQ's</li><li>About Us</li><li>Blog</li></ul></div>
<div class="abs foot-col" style="left:854px;top:4050px"><h4>Contact Info</h4>
  <div class="info-row"><svg width="14" height="12" viewBox="0 0 16 12"><rect width="16" height="12" fill="var(--blue)"/><path d="M0 0l8 6 8-6" stroke="#232323" stroke-width="1.4" fill="none"/></svg><span>Email:<br>hello@finishmail.ch</span></div>
  <div class="info-row"><svg width="14" height="14" viewBox="0 0 24 24"><path fill="var(--blue)" d="M6.6 10.8a15 15 0 006.6 6.6l2.2-2.2a1 1 0 011-.25 11.4 11.4 0 003.6.6 1 1 0 011 1V20a1 1 0 01-1 1A17 17 0 013 4a1 1 0 011-1h3.5a1 1 0 011 1c0 1.25.2 2.45.6 3.6a1 1 0 01-.25 1z"/></svg><span>Phone:<br>(041) 555-0182</span></div>
  <div class="info-row"><svg width="14" height="16" viewBox="0 0 12 16"><path fill="var(--blue)" d="M6 0a6 6 0 00-6 6c0 4.5 6 10 6 10s6-5.5 6-10a6 6 0 00-6-6zm0 8.5A2.5 2.5 0 116 3.5a2.5 2.5 0 010 5z"/></svg><span>Location:<br>12 Quay Lane, Unit 4</span></div>
</div>
<div class="ph" style="left:90px;top:4334px;width:1020px;height:1px;background:#444"></div>
<div class="abs copyright">Copyright 2023 All Rights Reserved</div>
<svg class="ph" style="left:1136px;top:4306px" width="48" height="48"><circle cx="24" cy="24" r="24" fill="var(--blue)"/><path d="M14 18h20v12H22l-5 4v-4h-3z" fill="#fff"/></svg>

</body>
</html>
```